Cover for a progress report

I need someone to take the following photo and add words to it in a way where it looks like a professional cover for a printed booklet.
The size of the book is landscape 6X9… 9 being the horizontal length ... there is a 1/4 inch safe zone around the photo that can't contain words.
I need the following words on it somehow as well as the attached logo
2022
Harrowfield Links Trust
Progress Report
I have to have this done by 3 p.m. CST tomorrow, so time is of the essence. I have attached the colors that are used throughout the entire book.

```html
<!DOCTYPE html>
<html lang="en">
<head>
<meta charset="utf-8">
<title>Harrowfield Links Trust — 2022 Progress Report</title>
<link href="https://fonts.googleapis.com/css2?family=Saira+Extra+Condensed:wght@600;700&display=swap" rel="stylesheet">
<style>
  :root{
    --trust-red:#A3282F;
    --trust-navy:#20325C;
    --paper:#FFFFFF;
    --turf-light:#9DA85A;
    --turf-dark:#5E7033;
    --canopy:#3E5530;
    --autumn:#B9803E;
    --sky:#E4E6E4;
  }
  *{margin:0;padding:0;box-sizing:border-box;}
  html,body{width:1200px;height:783px;overflow:hidden;background:var(--paper);}
  .cover{
    position:relative;width:1200px;height:783px;background:var(--paper);
    font-family:"Saira Extra Condensed","Arial Narrow",sans-serif;color:var(--paper);
  }
  .cover-photo{
    position:absolute;left:0;top:0;width:860px;height:573px;
    background:
      linear-gradient(180deg, var(--sky) 0%, rgba(228,230,228,0) 22%),
      radial-gradient(ellipse at 20% 20%, var(--autumn) 0%, rgba(185,128,62,0) 35%),
      linear-gradient(180deg, var(--canopy) 0%, var(--canopy) 40%, var(--turf-light) 55%, var(--turf-dark) 100%);
  }
  .brand-panel{
    position:absolute;left:873px;top:0;width:327px;height:573px;
    background:var(--trust-navy);
    display:flex;align-items:center;justify-content:center;gap:14px;
  }
  .brand-mark{width:22px;height:22px;border-radius:50%;background:var(--paper);}
  .brand-name{font-size:84px;font-weight:700;line-height:1;letter-spacing:2px;color:var(--paper);}
  .title-band{
    position:absolute;left:0;top:587px;width:1200px;height:196px;
    display:block;
  }
  .title-band .band-fill{fill:var(--trust-red);}
  .title-band .label-box{fill:var(--trust-navy);}
  .title-band text{
    fill:var(--paper);
    font-family:"Saira Extra Condensed","Arial Narrow",sans-serif;
    text-transform:uppercase;
  }
  .report-year{font-size:150px;font-weight:700;}
  .org-name{font-size:44px;font-weight:600;}
  .report-label{font-size:68px;font-weight:600;}
</style>
</head>
<body>
  <main class="cover">
    <div class="cover-photo" role="img" aria-label="Photograph of two golfers seated on a bench beside a practice range, autumn trees and fairway behind them"></div>
    <div class="brand-panel">
      <span class="brand-mark"></span>
      <span class="brand-name">HLT</span>
    </div>
    <svg class="title-band" viewBox="0 0 1200 196" width="1200" height="196">
      <rect class="band-fill" x="0" y="0" width="1200" height="196"/>
      <text class="report-year" x="304" y="145" textLength="214" lengthAdjust="spacingAndGlyphs">2022</text>
      <text class="org-name" x="534" y="68" textLength="361" lengthAdjust="spacingAndGlyphs">Harrowfield Links Trust</text>
      <rect class="label-box" x="538" y="80" width="357" height="65"/>
      <text class="report-label" x="545" y="137" textLength="343" lengthAdjust="spacingAndGlyphs">Progress Report</text>
    </svg>
  </main>
</body>
</html>
```